hi all

Im after a new age looking business card with my company logo on it

must include these details, I would like the PH and Email to be symbols

If the colours used for card could be kept within the colours used in logo that I have supplied that would be great, if another colour is to be used dark grey would be ok. no light bulbs etc thanks

Details below to be incorporated on card

Damian Holloway

Lic E871302

PH 0219647381

E info@brightvaleelectrical.example.nz

Domestic Commercial Industrial Electricians

```html
<!DOCTYPE html>
<html lang="en">
<head>
<meta charset="utf-8">
<title>Brightvale Electrical – Business Card</title>
<link href="https://fonts.googleapis.com/css2?family=Poppins:wght@400;500;700&display=swap" rel="stylesheet">
<style>
  :root {
    --stage: #8e8f91;
    --card-white: #f7f7f7;
    --brand-blue: #1f6fc4;
    --brand-deep: #1a4fa8;
    --brand-cyan: #4fc3e8;
    --ink-grey: #3c3c3c;
    --text-light: #dbeeff;
  }
  * { margin: 0; padding: 0; box-sizing: border-box; }
  html, body { width: 1200px; height: 801px; overflow: hidden; }
  body {
    background: var(--stage);
    font-family: "Poppins", sans-serif;
    display: flex;
    align-items: center;
    justify-content: center;
    gap: 50px;
  }
  .card {
    width: 520px;
    height: 300px;
    border-radius: 22px;
    position: relative;
    overflow: hidden;
    box-shadow: 0 10px 24px rgba(0,0,0,0.25);
  }
  /* Front */
  .card-front { background: var(--card-white); display: flex; align-items: center; }
  .front-brand {
    width: 250px;
    display: flex;
    flex-direction: column;
    align-items: center;
    gap: 10px;
  }
  .brand-mark {
    width: 46px; height: 46px; border-radius: 50%;
    background: var(--brand-blue);
  }
  .brand-name {
    font-weight: 700;
    font-size: 21px;
    letter-spacing: 1.5px;
    color: var(--brand-blue);
    text-transform: uppercase;
    text-align: center;
    line-height: 1.2;
  }
  .divider {
    width: 1px; height: 140px; background: var(--brand-blue);
  }
  .front-details { padding-left: 26px; }
  .holder-name {
    font-weight: 700; font-size: 19px; color: var(--brand-blue);
    text-transform: uppercase; letter-spacing: 0.5px; margin-bottom: 8px;
  }
  .contact-list { list-style: none; }
  .contact-item {
    display: flex; align-items: center; gap: 7px;
    font-size: 11.5px; color: var(--ink-grey); line-height: 1.75;
  }
  .contact-item svg { width: 11px; height: 11px; fill: var(--brand-deep); flex: none; }
  .licence { font-size: 11.5px; color: var(--ink-grey); margin-top: 6px; }
  /* Back */
  .card-back {
    background: linear-gradient(135deg, #2a82d6, var(--brand-blue) 60%, #1b64b8);
    display: flex; flex-direction: column; align-items: center; justify-content: center;
  }
  .back-brand { display: flex; flex-direction: column; align-items: center; gap: 12px; margin-top: -20px; }
  .back-brand .brand-mark { width: 58px; height: 58px; background: var(--brand-cyan); }
  .back-brand .brand-name { color: var(--brand-cyan); font-size: 32px; letter-spacing: 2.5px; }
  .services {
    position: absolute; bottom: 30px; left: 0; right: 0;
    display: flex; justify-content: center; align-items: center; gap: 9px;
    font-size: 12px; letter-spacing: 1px; color: var(--text-light); text-transform: uppercase;
  }
  .services svg { width: 8px; height: 14px; fill: var(--text-light); }
</style>
</head>
<body>
  <section class="card card-front">
    <div class="front-brand">
      <div class="brand-mark"></div>
      <div class="brand-name">Brightvale<br>Electrical</div>
    </div>
    <div class="divider"></div>
    <div class="front-details">
      <h1 class="holder-name">Damian Holloway</h1>
      <ul class="contact-list">
        <li class="contact-item">
          <svg viewBox="0 0 24 24"><path d="M6.6 10.8a15.1 15.1 0 0 0 6.6 6.6l2.2-2.2a1 1 0 0 1 1-.25 11.4 11.4 0 0 0 3.6.57 1 1 0 0 1 1 1V20a1 1 0 0 1-1 1A17 17 0 0 1 3 4a1 1 0 0 1 1-1h3.5a1 1 0 0 1 1 1c0 1.25.2 2.45.57 3.57a1 1 0 0 1-.25 1z"/></svg>
          0219647381
        </li>
        <li class="contact-item">
          <svg viewBox="0 0 24 24"><path d="M2 5h20v14H2z M2 5l10 8 10-8" stroke="#fff" stroke-width="1.5"/></svg>
          info@brightvaleelectrical.example.nz
        </li>
        <li class="contact-item">
          <svg viewBox="0 0 24 24"><circle cx="12" cy="12" r="10"/></svg>
          brightvaleelectrical.example.nz
        </li>
      </ul>
      <p class="licence">LIC : E871302</p>
    </div>
  </section>

  <section class="card card-back">
    <div class="back-brand">
      <div class="brand-mark"></div>
      <div class="brand-name">Brightvale Electrical</div>
    </div>
    <div class="services">
      <span>Domestic</span>
      <svg viewBox="0 0 8 14"><path d="M5 0 0 8h3l-1 6 6-9H5z"/></svg>
      <span>Commercial</span>
      <svg viewBox="0 0 8 14"><path d="M5 0 0 8h3l-1 6 6-9H5z"/></svg>
      <span>Industrial</span>
      <svg viewBox="0 0 8 14"><path d="M5 0 0 8h3l-1 6 6-9H5z"/></svg>
      <span>Electricians</span>
    </div>
  </section>
</body>
</html>
```